Need a business card for a Construction and Remodeling company.
Our company logo is the fleur de lis design as thats the family crust that we use on our logos.
Heres the info it needs:

Brackmore Construction & Remodeling, LLC
Renovations * Restorations

Elwin R. Brackmore
845 North Quarry Road
Millbrook Connecticut 06012
(203) 555.0182
CT LIC/REG: 418257

home owners, customers

```html
<!DOCTYPE html>
<html lang="en">
<head>
<meta charset="utf-8">
<title>Brackmore Construction &amp; Remodeling – Business Card</title>
<link rel="stylesheet" href="https://fonts.googleapis.com/css2?family=Cinzel:wght@400;600&family=Source+Sans+3:wght@400;600&display=swap">
<style>
  :root {
    --backdrop: #262626;
    --card: #141414;
    --card-edge: #1c1c1c;
    --emboss: #2a2a2a;
    --ink: #e6e6e6;
    --muted: #bdbdbd;
    --gold: #c9a03c;
  }
  * { box-sizing: border-box; margin: 0; padding: 0; }
  html, body {
    width: 1200px; height: 900px; overflow: hidden;
    background: var(--backdrop);
  }
  .stage { position: relative; width: 1200px; height: 900px; }
  .card {
    position: absolute; left: 240px; width: 720px; height: 411px;
    background: var(--card);
    border: 1px solid var(--card-edge);
    box-shadow: 0 10px 30px rgba(0,0,0,.45);
    overflow: hidden;
  }
  .card--front { top: 30px; }
  .card--back { top: 459px; }

  .front-mark {
    position: absolute; inset: 0;
    display: flex; flex-direction: column; align-items: center; justify-content: center; gap: 22px;
  }
  .front-mark .dot {
    width: 46px; height: 46px; border-radius: 50%;
    background: var(--emboss);
  }
  .front-mark .company {
    font-family: "Cinzel", serif; font-weight: 600; font-size: 30px;
    color: var(--emboss); text-align: center; line-height: 1.25; max-width: 520px;
  }

  .holder { position: absolute; left: 60px; top: 52px; }
  .holder .name {
    font-family: "Cinzel", serif; font-weight: 400; font-size: 22px;
    color: var(--ink); letter-spacing: 1.5px;
  }
  .holder .licence {
    font-family: "Source Sans 3", sans-serif; font-size: 14px; color: var(--gold);
    margin-top: 2px; letter-spacing: .3px;
  }

  .contact {
    position: absolute; left: 60px; top: 205px; list-style: none;
    font-family: "Source Sans 3", sans-serif; font-size: 17px; color: var(--ink);
  }
  .contact li { display: flex; align-items: center; gap: 8px; height: 26px; }
  .contact svg { width: 16px; height: 16px; flex: none; }
  .contact .city { padding-left: 24px; color: var(--muted); }

  .brand {
    position: absolute; right: 50px; top: 250px; width: 340px;
    display: flex; flex-direction: column; align-items: center;
  }
  .brand .dot {
    width: 38px; height: 38px; border-radius: 50%; background: var(--gold);
    margin-bottom: 14px;
  }
  .brand .company {
    font-family: "Cinzel", serif; font-weight: 400; font-size: 21px;
    color: var(--ink); text-align: center; line-height: 1.3;
  }
  .services {
    display: flex; gap: 12px; margin-top: 16px;
    font-family: "Source Sans 3", sans-serif; font-size: 17px; color: var(--gold);
  }
</style>
</head>
<body>
<main class="stage">
  <section class="card card--front" aria-label="Card front">
    <div class="front-mark">
      <span class="dot"></span>
      <p class="company">Brackmore Construction &amp; Remodeling, LLC</p>
    </div>
  </section>

  <section class="card card--back" aria-label="Card back">
    <header class="holder">
      <p class="name">ELWIN R. BRACKMORE</p>
      <p class="licence">LIC/REG: 418257</p>
    </header>

    <ul class="contact">
      <li>
        <svg viewBox="0 0 16 16" aria-hidden="true"><path fill="var(--gold)" d="M2 6c0-2 2-3 6-3s6 1 6 3v1h-3V5.5H5V7H2zM4 8h8l1.5 5h-11z"/></svg>
        (203) 555-0182
      </li>
      <li>
        <svg viewBox="0 0 16 16" aria-hidden="true"><rect x="1.5" y="3.5" width="13" height="9" fill="none" stroke="var(--gold)" stroke-width="1.5"/><path d="M1.5 3.5 8 9l6.5-5.5" fill="none" stroke="var(--gold)" stroke-width="1.5"/></svg>
        office@brackmorebuild.com
      </li>
      <li>
        <svg viewBox="0 0 16 16" aria-hidden="true"><path fill="var(--gold)" d="M8 1a5 5 0 0 0-5 5c0 4 5 9 5 9s5-5 5-9a5 5 0 0 0-5-5zm0 7a2 2 0 1 1 0-4 2 2 0 0 1 0 4z"/></svg>
        845 North Quarry Road
      </li>
      <li class="city">Millbrook Connecticut 06012</li>
    </ul>

    <div class="brand">
      <span class="dot"></span>
      <p class="company">Brackmore Construction &amp; Remodeling, LLC</p>
      <p class="services"><span>Renovations</span><span>|</span><span>Additions</span><span>|</span><span>Restorations</span></p>
    </div>
  </section>
</main>
</body>
</html>
```